Fiscal Sponsorship Program Flyer

We are seeking a designer to create a 1-2 flyer that explains our fiscal sponsorship program. This flyer will be used to recruit new projects that might be interested in utilizing our fiscal sponsorship services. The pertinent information about our program can be found in the attached PDF. For users who cannot access the PDF, please try this link: https://files.brivanto.net/slides/d/7QtR2wXkLmZp9HvCs4YdNe8JfGaUoBi3Tx5Wl0KyRc2s/view?mode=shared

Target Market(s)

New charitable projects that do not yet have their own 501(c)(3) status, and are seeking a fiscal sponsor.

Industry/Entity Type

Nonprofit/Charity

Requirements
Must have
• The flyer must include the language and detail included on the attached PDF. The desire is to reformat this to be more appealing and easy to read.

```html
<!DOCTYPE html>
<html lang="en">
<head>
<meta charset="utf-8">
<title>Harbor Foundation – Fiscal Sponsorship Program Flyer</title>
<link href="https://fonts.googleapis.com/css2?family=Tinos:wght@700&family=Raleway:wght@500;600;700;800&display=swap" rel="stylesheet">
<style>
:root{
  --red:#f2514f;
  --red-deep:#e3332c;
  --navy:#1b2633;
  --slate:#4a5859;
  --charcoal:#2e3438;
  --ink:#333;
  --white:#fff;
  --yellow:#ffe13a;
  --stage:#d9d9d9;
}
*{box-sizing:border-box;margin:0;padding:0}
html,body{width:1200px;height:930px;overflow:hidden}
body{background:var(--stage);font-family:"Raleway",Arial,sans-serif;position:relative}
.serif{font-family:"Tinos","Times New Roman",serif;font-weight:700}
.page{position:absolute;top:93px;width:527px;height:743px;background:var(--white);overflow:hidden}
.page--front{left:53px}
.page--back{left:624px;width:526px}
.abs{position:absolute}

/* front */
.hero-photo{left:0;top:0;width:100%;height:190px;background:linear-gradient(160deg,#1a2432,#22344a 55%,#162029)}
.red-band{left:0;top:400px;width:100%;height:343px;background:linear-gradient(180deg,var(--red),var(--red-deep))}
.title{left:0;width:100%;text-align:center}
.title--main{top:30px;font-size:47px;color:var(--red);line-height:1.1}
.title--sub{top:86px;font-size:31px;color:var(--white)}
.mission-box{left:32px;top:157px;width:463px;height:88px;background:var(--red);border-radius:6px;display:flex;padding:26px 20px 0}
.mission-box p{flex:1;color:var(--white);font-size:8.4px;font-weight:700;line-height:1.45}
.mission-box p:first-child{padding-right:10px;border-right:1.5px solid var(--white)}
.mission-box p:last-child{padding-left:12px}
.pill-dark{left:153px;top:140px;width:221px;height:34px;background:var(--charcoal);border-radius:6px;color:var(--white);font-size:22px;text-align:center;line-height:34px;box-shadow:0 2px 3px rgba(0,0,0,.35)}
.section-heading{left:0;width:100%;text-align:center;font-size:22px;color:var(--ink)}
.intro{left:64px;top:284px;width:399px;text-align:center;font-size:8.4px;line-height:1.4;color:var(--ink)}
.card{top:340px;width:229px;height:213px;background:var(--slate);border-radius:8px;padding:12px 14px;color:var(--white);box-shadow:0 2px 5px rgba(0,0,0,.3)}
.card h3{font-size:14px;line-height:1.15;height:34px;max-width:190px}
.card .rule{height:2px;background:#8a9596;margin:7px 0 10px;position:relative}
.card .rule::before{content:"";position:absolute;left:0;top:0;width:64px;height:2px;background:var(--red)}
.card p,.card li{font-size:8.2px;line-height:1.4;font-weight:500}
.card p+p{margin-top:8px}
.card ul{list-style:none;margin-top:9px}
.card li{display:flex;gap:9px;margin-bottom:6px}
.tick{flex:none;width:10px;height:10px;margin-top:1px}
.values-heading{left:32px;top:572px;width:463px;display:flex;align-items:center;gap:12px;color:var(--white);font-size:22px}
.values-heading::before,.values-heading::after{content:"";flex:1;height:1.5px;background:var(--charcoal)}
.values{left:32px;top:607px;width:463px;display:grid;grid-template-columns:1fr 1fr;column-gap:20px}
.value{display:flex;gap:10px;margin-bottom:8px;font-size:8.4px;line-height:1.4;color:var(--white);font-weight:500}
.value b{color:var(--yellow);font-weight:800}
.value svg{flex:none;width:22px;height:22px}
.values .col-right{border-left:1px solid rgba(0,0,0,.15);padding-left:14px}

/* back */
.commit-photo{left:0;top:0;width:100%;height:270px;background:linear-gradient(160deg,#2a3034,#3b4347 50%,#262b2e)}
.commit-title{left:0;top:30px;width:100%;text-align:center;font-size:22px;color:var(--red)}
.commit-list{top:68px;list-style:none}
.commit-list li{display:flex;gap:10px;font-size:10.2px;line-height:1.45;color:var(--white);font-weight:500;margin-bottom:10px}
.commit-list--a{left:30px;width:210px}
.commit-list--b{left:262px;width:240px;border-left:1.5px solid var(--red);padding-left:12px;height:150px}
.commit-list--b li{margin-bottom:13px}
.commit-list .tick{width:12px;height:12px;margin-top:2px}
.fee-pill{left:116px;top:252px;width:294px;height:39px;background:var(--red);border-radius:7px;text-align:center;line-height:40px;font-size:26px;color:var(--charcoal);box-shadow:0 2px 3px rgba(0,0,0,.25)}
.tier{top:305px;width:151px;height:418px;border-radius:8px;background:linear-gradient(180deg,var(--red),var(--red-deep));padding:20px 8px 0 20px;color:var(--white);box-shadow:0 2px 4px rgba(0,0,0,.2);overflow:hidden}
.tier--basic{left:30px}
.tier--standard{left:185px;padding-left:16px}
.tier--premium{left:340px;padding-left:15px}
.tier h3{font-size:24px;line-height:1.15;color:var(--charcoal);height:70px}
.tier .tag{width:114px;height:22px;background:var(--charcoal);color:var(--white);font-size:12px;font-weight:700;text-align:center;line-height:22px;margin-bottom:10px}
.tier--basic .tag{text-align:left;padding-left:14px}
.tier .lead{font-size:10px;font-weight:700;line-height:1.42;margin-bottom:11px}
.tier ul{list-style:none}
.tier li{position:relative;padding-left:22px;font-size:10px;font-weight:700;line-height:1.42;margin-bottom:10px}
.tier li::before{content:"";position:absolute;left:2px;top:5px;width:5px;height:5px;border-radius:50%;background:var(--charcoal)}
.tier--basic li{margin-bottom:10px}
.tier--standard li{margin-bottom:16px}
.tier--premium li{margin-bottom:8px}
</style>
</head>
<body>

<section class="page page--front">
  <div class="abs hero-photo" role="img" aria-label="Dark blue photo of a handshake over a digital network backdrop"></div>
  <div class="abs red-band"></div>

  <h1 class="abs title title--main serif">Harbor Foundation</h1>
  <h2 class="abs title title--sub serif">Fiscal Sponsorship Program</h2>

  <div class="abs mission-box">
    <p>The Harbor Foundation, founded in 2010, exists to support social impact campaigns and organizations through educational, public engagement, and awareness efforts.</p>
    <p>Its vision is to strengthen the capacity of the social impact sector and its leaders by providing top-tier fiscal sponsorship services.</p>
  </div>
  <div class="abs pill-dark serif">Mission &amp; Vision</div>

  <h2 class="abs section-heading serif" style="top:252px">What is Fiscal Sponsorship?</h2>
  <p class="abs intro">Fiscal sponsorship refers to the practice of non-profit organizations offering their legal and tax-exempt status to charitable projects or groups engaged in activities related to the sponsoring organization's mission. Fiscal sponsors provide oversight, financial management, and other administrative services to build the capacity of charitable projects.</p>

  <article class="abs card" style="left:32px">
    <h3 class="serif">What kinds of projects are eligible for fiscal sponsorship?</h3>
    <div class="rule"></div>
    <p>Harbor Foundation uses the following broad criteria to determine whether or not a project is eligible for fiscal sponsorship:</p>
    <ul>
      <li><svg class="tick" viewBox="0 0 10 10"><circle cx="5" cy="5" r="5" fill="#f2514f"/><path d="M2.6 5.1l1.6 1.6 3.2-3.3" stroke="#fff" stroke-width="1.3" fill="none"/></svg><span>Mission alignment with the Harbor Foundation;</span></li>
      <li><svg class="tick" viewBox="0 0 10 10"><circle cx="5" cy="5" r="5" fill="#f2514f"/><path d="M2.6 5.1l1.6 1.6 3.2-3.3" stroke="#fff" stroke-width="1.3" fill="none"/></svg><span>Whether or not the project provides an educational, social or charitable benefit; and</span></li>
      <li><svg class="tick" viewBox="0 0 10 10"><circle cx="5" cy="5" r="5" fill="#f2514f"/><path d="M2.6 5.1l1.6 1.6 3.2-3.3" stroke="#fff" stroke-width="1.3" fill="none"/></svg><span>Whether or not the project's activities follow the IRS regulations governing 501© (3) public charities.</span></li>
    </ul>
  </article>

  <article class="abs card" style="left:263px">
    <h3 class="serif" style="max-width:150px">Fiscal Sponsorship Program Philosophy</h3>
    <div class="rule"></div>
    <p>We believe we can accelerate the pace and scale of social change by providing strategic back office support to emerging projects, leaders and ideas.</p>
    <p>By providing light touch administrative and capacity building services, our fiscal sponsorship program takes the administrative burden off the shoulders of leaders and their projects to allow them to focus on what they do best - achieving impact and changing the world.</p>
  </article>

  <h2 class="abs values-heading serif">Organizational Values</h2>
  <div class="abs values">
    <div class="col-left">
      <div class="value"><svg viewBox="0 0 22 22"><circle cx="11" cy="11" r="11" fill="#2e3438"/><path d="M5 12l3-3 3 2 3-2 3 3-3 3h-6z" fill="none" stroke="#fff" stroke-width="1.2"/></svg><p><b>TRUST:</b> We believe that all successful partnerships begin with a foundation of trust.</p></div>
      <div class="value"><svg viewBox="0 0 22 22"><circle cx="11" cy="11" r="11" fill="#2e3438"/><circle cx="11" cy="9" r="3.5" fill="none" stroke="#fff" stroke-width="1.2"/><path d="M9.5 13h3v3h-3z" fill="#fff"/></svg><p><b>INNOVATION:</b> We embrace continuous improvement, bold creativity and change.</p></div>
      <div class="value"><svg viewBox="0 0 22 22"><circle cx="11" cy="11" r="11" fill="#2e3438"/><circle cx="11" cy="11" r="4" fill="none" stroke="#fff" stroke-width="1.4" stroke-dasharray="2 1.5"/><circle cx="11" cy="11" r="1.5" fill="#fff"/></svg><p><b>EMBRACE COMPLEXITY AND RISK:</b> We understand that bold solutions to intractable social issues often require both complexity and risk.</p></div>
    </div>
    <div class="col-right">
      <div class="value"><svg viewBox="0 0 22 22"><circle cx="11" cy="11" r="11" fill="#2e3438"/><path d="M11 16l-5-5a2.6 2.6 0 0 1 5-3 2.6 2.6 0 0 1 5 3z" fill="none" stroke="#fff" stroke-width="1.2"/></svg><p><b>DIVERSITY:</b> We believe that all voices matter and that effective solutions are created when decision-making is inclusive across social, cultural and economic backgrounds.</p></div>
      <div class="value"><svg viewBox="0 0 22 22"><circle cx="11" cy="11" r="11" fill="#2e3438"/><circle cx="11" cy="11" r="4.5" fill="none" stroke="#fff" stroke-width="1.2"/><circle cx="11" cy="11" r="1.6" fill="#fff"/></svg><p><b>RELATIONSHIPS:</b> Our partners are central to our work. We honor our relationships through respect, communication and transparency.</p></div>
    </div>
  </div>
</section>

<section class="page page--back">
  <div class="abs commit-photo" role="img" aria-label="Dimmed photo of a team joining hands in celebration"></div>
  <h2 class="abs commit-title serif">Harbor Foundation - Program Commitments</h2>

  <ul class="abs commit-list commit-list--a">
    <li><svg class="tick" viewBox="0 0 10 10"><circle cx="5" cy="5" r="5" fill="#f2514f"/><path d="M2.6 5.1l1.6 1.6 3.2-3.3" stroke="#fff" stroke-width="1.3" fill="none"/></svg><span>Fast, simple and efficient fiscal sponsorship program</span></li>
    <li><svg class="tick" viewBox="0 0 10 10"><circle cx="5" cy="5" r="5" fill="#f2514f"/><path d="M2.6 5.1l1.6 1.6 3.2-3.3" stroke="#fff" stroke-width="1.3" fill="none"/></svg><span>No fees and no minimums; projects of any size are welcome to apply</span></li>
    <li><svg class="tick" viewBox="0 0 10 10"><circle cx="5" cy="5" r="5" fill="#f2514f"/><path d="M2.6 5.1l1.6 1.6 3.2-3.3" stroke="#fff" stroke-width="1.3" fill="none"/></svg><span>Easy onboarding process</span></li>
    <li><svg class="tick" viewBox="0 0 10 10"><circle cx="5" cy="5" r="5" fill="#f2514f"/><path d="M2.6 5.1l1.6 1.6 3.2-3.3" stroke="#fff" stroke-width="1.3" fill="none"/></svg><span>Complex, hybrid structures, partnerships and coalitions are strongly encouraged to apply</span></li>
  </ul>
  <ul class="abs commit-list commit-list--b">
    <li><svg class="tick" viewBox="0 0 10 10"><circle cx="5" cy="5" r="5" fill="#f2514f"/><path d="M2.6 5.1l1.6 1.6 3.2-3.3" stroke="#fff" stroke-width="1.3" fill="none"/></svg><span>Free and fast approval process - our application can be completed in 30 minutes or less. There is no fee to apply, and most projects can expect to receive a response on their application within 2 weeks</span></li>
    <li><svg class="tick" viewBox="0 0 10 10"><circle cx="5" cy="5" r="5" fill="#f2514f"/><path d="M2.6 5.1l1.6 1.6 3.2-3.3" stroke="#fff" stroke-width="1.3" fill="none"/></svg><span>Dedicated customer service and customization of services, tailored to the individual sponsored project's needs</span></li>
  </ul>

  <div class="abs fee-pill serif">FEE STRUCTURE</div>

  <article class="abs tier tier--basic">
    <h3 class="serif">Basic |<br>Fee - 4%</h3>
    <div class="tag">Limited</div>
    <ul>
      <li>Project Fund Set-Up</li>
      <li>Administration and Management</li>
      <li>Financial Management</li>
      <li>Grant Proposal Review</li>
      <li>Grant Contract Review</li>
      <li>Project Reporting</li>
      <li>Insurance</li>
      <li>Annual Audit and Form 990</li>
    </ul>
  </article>

  <article class="abs tier tier--standard">
    <h3 class="serif">Standard |<br>Fee - 6%</h3>
    <div class="tag">Comprehensive</div>
    <p class="lead">BASIC SERVICES •</p>
    <ul>
      <li>Customized Financial Reporting</li>
      <li>Monthly Financial Statements</li>
      <li>Subgranting/ regranting to U.S.-based organizations</li>
      <li>Management of Vendor and Independent Contractors (1099s)</li>
    </ul>
  </article>

  <article class="abs tier tier--premium">
    <h3 class="serif">Premium |<br>Fee - 10% +</h3>
    <div class="tag">Custom</div>
    <p class="lead" style="font-weight:600">Standard Services • custom services tailored to individual project needs.</p>
    <p class="lead">CUSTOMIZATION OPTIONS:</p>
    <ul>
      <li>Subgranting/ regranting to international organizations</li>
      <li>Lobbying Filings</li>
      <li>Project Audit</li>
      <li>Grant Writing Assistance</li>
      <li>One-on-One Coaching</li>
    </ul>
  </article>
</section>

</body>
</html>
```